Les Aliments Fortaleoni 2 sided flyer

We have a restaurant in St.Ambrelle, Montreal east, called Restaurant Fortaleoni and now we are bringing our product (food) to the South Shore of Montreal in Brossard as Les Aliments Fortaleoni not as a restaurant but as a frozen food store.

- We are a frozen store. (not a restaurant just a reminder) (almost like a grocery store)
- Selling homemade Italian food prepared in location, frozen and vacuumed packed.

- I need flyers telling the public that we are Bringing Fortaleoni's (frozen food) to the South Shore with my logo, few picture, and my location.

Industry/Entity Type

Food Production

Font styles to use
Sans Serif

Colors
ffffff
000000

Requirements
Must have
• address: 4137 Boul. Vermandois
• Brossard, Quebec
• J7K 2B9
• our email address : alimentsfortaleoni@courrielnet.ca
• -flyer must be in french, i can supply the translation if needed
• needs to be refreshing, appealing, and attract the public
Nice to have
• the color burgundy is not available would like to see how it looks with that color to match my sign and logo
• the flyer has to be in french because I live in Quebec and its the law here
Should not have
• should not hurt the eyes when reading

```html
<!DOCTYPE html>
<html lang="fr">
<head>
<meta charset="utf-8">
<title>Les Aliments Fortaleoni – Flyer</title>
<link rel="stylesheet" href="https://fonts.googleapis.com/css2?family=Arimo:wght@700&family=Oswald:wght@500&display=swap">
<style>
  :root {
    --stage: #e9e6e3;
    --white: #ffffff;
    --black: #000000;
    --burgundy: #a51f2b;
    --panel: rgba(255, 255, 255, 0.72);
    --pill: rgba(255, 255, 255, 0.78);
    --pizza-light: #f6c85a;
    --pizza-mid: #e59a32;
    --pizza-deep: #a8561c;
    --crust: #6e3a17;
  }
  * { box-sizing: border-box; margin: 0; padding: 0; }
  html, body { width: 1200px; height: 960px; overflow: hidden; }
  body { background: var(--stage); position: relative; font-family: "Arimo", Arial, sans-serif; }

  .flyer {
    position: absolute; left: 288px; top: 40px;
    width: 624px; height: 880px; overflow: hidden;
    box-shadow: 0 10px 30px rgba(0,0,0,0.25);
  }
  .flyer__photo {
    position: absolute; inset: 0;
    background:
      radial-gradient(ellipse 70% 55% at 50% 62%, var(--pizza-light) 0%, var(--pizza-mid) 55%, var(--pizza-deep) 85%, var(--crust) 100%);
  }
  .flyer__corners { position: absolute; inset: 0; }

  .brand-panel {
    position: absolute; left: 49px; top: 99px; width: 525px; height: 322px;
    background: var(--panel); border-radius: 22px;
  }
  .brand-panel__brackets { position: absolute; left: 35px; top: 85px; }

  .brand {
    position: absolute; left: 49px; width: 525px; text-align: center;
    font-family: "Oswald", "Arial Narrow", sans-serif; font-weight: 500;
    color: var(--burgundy); text-transform: uppercase;
  }
  .brand--small { top: 135px; font-size: 40px; letter-spacing: 8px; }
  .brand--large { top: 188px; font-size: 92px; line-height: 1.05; letter-spacing: 2px; }

  .since {
    position: absolute; left: 49px; top: 325px; width: 525px;
    display: flex; align-items: center; justify-content: center; gap: 14px;
    font-family: "Oswald", "Arial Narrow", sans-serif; font-weight: 500;
    font-size: 30px; color: var(--black);
  }
  .since__rule { display: block; width: 125px; height: 4px; background: var(--black); }

  .email {
    position: absolute; left: 49px; top: 380px; width: 525px; text-align: center;
    font-size: 19px; color: var(--black);
  }

  .dish {
    position: absolute; border-radius: 50%; border: 6px solid var(--white);
    box-shadow: 0 4px 14px rgba(0,0,0,0.35);
  }
  .dish--lasagna { left: 48px; top: 473px; width: 150px; height: 150px;
    background: radial-gradient(circle at 50% 55%, #d9a24a, #9c5a22 70%, #f2efe9 100%); }
  .dish--pizza { left: 199px; top: 433px; width: 224px; height: 224px;
    background: radial-gradient(circle at 50% 50%, #f5cd63, #e2a23c 70%, #7b4a1e 100%); }
  .dish--sauce { left: 423px; top: 473px; width: 150px; height: 150px;
    background: radial-gradient(circle at 50% 60%, #d2381f, #a8231a 55%, #c9d2c6 100%); }

  .home-icon {
    position: absolute; left: 296px; top: 697px; width: 30px; height: 30px;
    border-radius: 50%; background: var(--white);
    display: flex; align-items: center; justify-content: center;
  }

  .address {
    position: absolute; left: 0; width: 624px;
    display: flex; justify-content: center; gap: 10px;
  }
  .address--street { top: 748px; }
  .address--postal { top: 790px; }
  .address__pill {
    background: var(--pill); color: var(--black);
    font-size: 22px; padding: 4px 10px; border-radius: 14px;
  }
</style>
</head>
<body>
  <main class="flyer">
    <div class="flyer__photo" role="img" aria-label="Photo en gros plan d'une pizza gratinée aux légumes"></div>

    <svg class="flyer__corners" width="624" height="880" viewBox="0 0 624 880" aria-hidden="true">
      <polygon points="0,0 70,0 0,45" fill="#ffffff"/>
      <polygon points="480,0 624,0 624,14" fill="#ffffff"/>
      <polygon points="0,870 0,880 180,880" fill="#ffffff"/>
      <polygon points="624,800 624,880 530,880" fill="#ffffff"/>
    </svg>

    <div class="brand-panel"></div>
    <svg class="brand-panel__brackets" width="554" height="350" viewBox="0 0 554 350" aria-hidden="true"
         style="position:absolute;left:35px;top:85px">
      <g fill="none" stroke="#ffffff" stroke-width="5" stroke-linecap="round">
        <path d="M3 60 V18 Q3 3 18 3 H60"/>
        <path d="M494 3 H536 Q551 3 551 18 V60"/>
        <path d="M3 290 V332 Q3 347 18 347 H60"/>
        <path d="M551 290 V332 Q551 347 536 347 H494"/>
      </g>
    </svg>

    <p class="brand brand--small">Les Aliments</p>
    <p class="brand brand--large">Fortaleoni</p>
    <p class="since"><span class="since__rule"></span>Depuis 1971<span class="since__rule"></span></p>
    <p class="email">alimentsfortaleoni@courrielnet.ca</p>

    <div class="dish dish--lasagna" role="img" aria-label="Photo d'une portion de lasagne gratinée"></div>
    <div class="dish dish--pizza" role="img" aria-label="Photo d'une pizza entière aux légumes"></div>
    <div class="dish dish--sauce" role="img" aria-label="Photo d'un pot de sauce tomate maison avec basilic"></div>

    <div class="home-icon" aria-hidden="true">
      <svg width="18" height="18" viewBox="0 0 24 24">
        <path d="M12 3 L2 12 H5 V21 H10 V15 H14 V21 H19 V12 H22 Z" fill="#000000"/>
      </svg>
    </div>

    <div class="address address--street">
      <span class="address__pill">4137 Boul. Vermandois</span>
      <span class="address__pill">Brossard, Quebec</span>
    </div>
    <div class="address address--postal">
      <span class="address__pill">J7K 2B9</span>
    </div>
  </main>
</body>
</html>
```